New business card for my lawn and landscape business

Dorrin Yard and Building is a full-service lawn care, landscaping, and light construction company serving Paragould and the Northeast Arkansas region. The business is owned and operated by Marcus Toller, with a reputation for hands-on, detail-oriented service, dependable crews, and quality results for both residential and commercial clients. A well regarded business with great reviews.
Owner Marcus Toller
Dorrinyardandbuilding.example

Target Market(s)

Commercial, Middle, and upper class in north east Arkansas

Industry/Entity Type

Lawn maintenance and landscape

Contact Information for Business Card

Dorrin Yard And Building Professional lawn care, landscaping, and property improvement in Northeast Arkansas. • lawn maintenance •lawn treatments and weed control • exterior projects • Custom landscape design & installation • Sod, trees, rock & drainage solutions • Residential & commercial services Reliable. Detailed. Done right.

Requirements
Must have
• Business name, service area, list of some of our services, clean design that represents
Nice to have
• Unique. Different design element than just grass because its already in n the logo. Picture of a warm season (south) lawn or landscape. Pictures of the type of work we do

```html
<!DOCTYPE html>
<html lang="en">
<head>
<meta charset="utf-8">
<title>Dorrin Yard and Building – Business Card</title>
<link href="https://fonts.googleapis.com/css2?family=Montserrat:wght@400;500;600;700;800&display=swap" rel="stylesheet">
<style>
  :root {
    --bg: #e9eaeb;
    --card: #ffffff;
    --green: #7cbd3b;
    --green-dark: #4f8f1f;
    --green-deep: #3d7a17;
    --grass-light: #8fd14a;
    --grass-dark: #3f8a1c;
    --gray-text: #5c5f62;
    --gray-line: #d9dbdc;
    --white: #ffffff;
  }
  * { margin: 0; padding: 0; box-sizing: border-box; }
  html, body { width: 1200px; height: 2480px; overflow: hidden; }
  body {
    background: var(--bg);
    font-family: "Montserrat", Arial, sans-serif;
    position: relative;
  }
  .card {
    position: absolute;
    left: 60px;
    width: 1080px;
    height: 620px;
    background: var(--card);
    border-radius: 28px;
    overflow: hidden;
    box-shadow: 0 10px 30px rgba(0,0,0,0.12);
  }
  .card-front { top: 520px; }
  .card-back { top: 1340px; }
  .card-shape { position: absolute; inset: 0; }

  /* front */
  .brand {
    position: absolute;
    left: 60px; top: 250px;
    display: flex; align-items: center; gap: 18px;
  }
  .brand-dot {
    width: 46px; height: 46px; border-radius: 50%;
    background: var(--green); flex: none;
  }
  .brand-name {
    font-weight: 700; font-size: 30px; line-height: 1.2;
    color: var(--gray-text); width: 300px;
    text-transform: uppercase; letter-spacing: 1px;
  }
  .owner {
    position: absolute; left: 560px; top: 150px; color: var(--white);
  }
  .owner-name { font-weight: 700; font-size: 52px; letter-spacing: 1px; text-transform: uppercase; }
  .owner-role { font-weight: 400; font-size: 30px; margin-top: 4px; }
  .contact-list {
    position: absolute; left: 560px; top: 340px; list-style: none; color: var(--white);
  }
  .contact-item {
    display: flex; align-items: center; gap: 18px;
    font-size: 26px; font-weight: 600; margin-bottom: 26px;
  }
  .contact-icon {
    width: 42px; height: 42px; border-radius: 50%;
    background: var(--white); display: flex; align-items: center; justify-content: center; flex: none;
  }

  /* back */
  .services-title {
    position: absolute; left: 56px; top: 44px;
    font-weight: 800; font-size: 50px; color: var(--green); letter-spacing: 1px;
  }
  .services-intro {
    position: absolute; left: 56px; top: 112px; width: 470px;
    font-size: 21px; line-height: 1.35; color: var(--gray-text);
  }
  .services-list {
    position: absolute; left: 56px; top: 228px; list-style: none;
    color: var(--green-dark); font-size: 22px; font-weight: 500;
  }
  .services-list li {
    display: flex; align-items: flex-start; gap: 14px; margin-bottom: 19px; line-height: 1.3;
  }
  .tick { flex: none; margin-top: 4px; }
</style>
</head>
<body>

<section class="card card-front">
  <svg class="card-shape" viewBox="0 0 1080 620" aria-hidden="true">
    <path d="M520 0 C420 150 420 470 560 620 L1080 620 L1080 0 Z" fill="var(--gray-line)"/>
    <path d="M545 0 C445 150 445 470 585 620 L1080 620 L1080 0 Z" fill="var(--green-deep)"/>
    <path d="M565 0 C465 150 465 470 605 620 L1080 620 L1080 0 Z" fill="var(--green)"/>
  </svg>

  <div class="brand">
    <span class="brand-dot"></span>
    <span class="brand-name">Dorrin Yard and Building</span>
  </div>

  <div class="owner" style="left:560px">
    <div class="owner-name">Marcus Toller</div>
    <div class="owner-role">Owner</div>
  </div>

  <ul class="contact-list">
    <li class="contact-item">
      <span class="contact-icon">
        <svg width="22" height="22" viewBox="0 0 24 24"><path fill="var(--green)" d="M6.6 10.8a15 15 0 0 0 6.6 6.6l2.2-2.2a1 1 0 0 1 1-.25 11.4 11.4 0 0 0 3.6.57 1 1 0 0 1 1 1V20a1 1 0 0 1-1 1A17 17 0 0 1 3 4a1 1 0 0 1 1-1h3.5a1 1 0 0 1 1 1c0 1.25.2 2.45.57 3.57a1 1 0 0 1-.25 1z"/></svg>
      </span>
      (870) 555-0142
    </li>
    <li class="contact-item">
      <span class="contact-icon">
        <svg width="24" height="24" viewBox="0 0 24 24" fill="none" stroke="var(--green)" stroke-width="2"><circle cx="12" cy="12" r="9"/><path d="M3 12h18M12 3c3 3 3 15 0 18M12 3c-3 3-3 15 0 18"/></svg>
      </span>
      Dorrinyardandbuilding.example
    </li>
  </ul>
</section>

<section class="card card-back">
  <svg class="card-shape" viewBox="0 0 1080 620">
    <defs>
      <linearGradient id="lawnTones" x1="0" y1="0" x2="0" y2="1">
        <stop offset="0" stop-color="var(--grass-light)"/>
        <stop offset="1" stop-color="var(--grass-dark)"/>
      </linearGradient>
    </defs>
    <path d="M600 0 C520 180 540 440 640 620 L1080 620 L1080 0 Z" fill="var(--green)"/>
    <path d="M630 0 C550 180 570 440 670 620 L1080 620 L1080 0 Z" fill="url(#lawnTones)" role="img" aria-label="Photo of a green lawn mower on freshly cut grass"/>
  </svg>

  <h2 class="services-title">OUR SERVICES</h2>
  <p class="services-intro">Dorrin Yard And Building Professional lawn care, landscaping, and property improvement in Northeast Arkansas.</p>

  <ul class="services-list">
    <li><svg class="tick" width="20" height="20" viewBox="0 0 20 20"><path d="M3 10l5 5 9-10" fill="none" stroke="var(--green)" stroke-width="3"/></svg>Lawn Maintenance</li>
    <li><svg class="tick" width="20" height="20" viewBox="0 0 20 20"><path d="M3 10l5 5 9-10" fill="none" stroke="var(--green)" stroke-width="3"/></svg>Exterior Projects</li>
    <li><svg class="tick" width="20" height="20" viewBox="0 0 20 20"><path d="M3 10l5 5 9-10" fill="none" stroke="var(--green)" stroke-width="3"/></svg>Sod, Trees, Rock &amp; Drainage Solutions</li>
    <li><svg class="tick" width="20" height="20" viewBox="0 0 20 20"><path d="M3 10l5 5 9-10" fill="none" stroke="var(--green)" stroke-width="3"/></svg>Lawn Treatments and Weed Control</li>
    <li><svg class="tick" width="20" height="20" viewBox="0 0 20 20"><path d="M3 10l5 5 9-10" fill="none" stroke="var(--green)" stroke-width="3"/></svg>Custom Landscape Design &amp; Installation</li>
    <li><svg class="tick" width="20" height="20" viewBox="0 0 20 20"><path d="M3 10l5 5 9-10" fill="none" stroke="var(--green)" stroke-width="3"/></svg><span>Residential &amp; Commercial Services<br>Reliable. Detailed. Done right.</span></li>
  </ul>
</section>

</body>
</html>
```